Premium men's gut health supplement needs a bottle label designed

We’re velnora - a premium men’s wellness brand focused on gut health. Our first product is a high-quality daily supplement designed to support digestion, regularity, and internal cleanliness. Backed by science and tailored for modern lifestyles, velnora is crafted in the UK and proudly LGBT-owned. It aims to resolve intimacy problems that gay men may experience due to poor digestion but also does not exclude any other orientation - other men may use it simply to improve their digestion.

velnora is for health-conscious men who value science-backed supplements and want to feel confident from the inside out. Many of our early adopters will be gay and bisexual men who prioritise gut health as part of their self-care, sexual, and hygiene routine, though the product is equally effective and appealing to anyone seeking premium digestive support.

The product is premium the target customer is male, not specific to one location but primary markets will be US, UK and EU.

I’d like a supplement bottle designed for velnora, our premium men’s gut health brand. The focus should be clean, slightly clinical, and minimal - inspired by brands like Quelrin and Darvo. The key element is the wordmark (velnora) on the front, with no additional logo or icon. Lowercase text and a strong, contemporary font are preferred.

The bottle should be aesthetically pleasing so that people are proud to display it on their shelf, instead of hiding it in a cupboard (like Quelrin, darvo, Pia Venturek, Morvanel etc)

Avoid anything that shows the product as being for LGBT, e.g., no rainbows, men holding hands etc.

The design should be premium, minimalist and not be busy or overwhelming.

I have uploaded a file called "Bottle" to give an idea of the type of container, but please ignore the colours and change as you see fit. This is just for reference for the type of bottle we'll use - all colours are customisable.

I have also uploaded some images for "style" reference, e.g., darvo, quelrin, pia venturek, etc for inspiration.

```html
<!DOCTYPE html>
<html lang="en">
<head>
<meta charset="utf-8">
<title>velnora – supplement label</title>
<link rel="stylesheet" href="https://fonts.googleapis.com/css2?family=Fredoka:wght@600&family=Overlock:wght@700&family=Questrial&display=swap">
<style>
  :root {
    --teal: #3d7286;
    --teal-light: #4a8aa0;
    --slate: #5d666b;
    --slate-dark: #1b2126;
    --ink: #0a0a0a;
    --cream: #ead6c4;
    --white: #ffffff;
    --paper: #ffffff;
  }
  * { box-sizing: border-box; margin: 0; padding: 0; }
  html, body { width: 1200px; height: 1200px; overflow: hidden; background: var(--paper); }
  .canvas { position: relative; width: 1200px; height: 1200px; }

  .label {
    position: absolute; top: 330px; width: 390px; height: 530px;
    color: var(--white);
  }
  .label--slate { left: 150px; background: linear-gradient(100deg, var(--slate) 0%, #2c3338 45%, var(--slate-dark) 100%); }
  .label--teal { left: 660px; background: linear-gradient(100deg, var(--teal) 0%, #41798d 50%, var(--teal-light) 100%); }

  .wordmark {
    position: absolute; left: 50px; top: 58px;
    font-family: "Fredoka", sans-serif; font-weight: 600;
    font-size: 86px; line-height: 1; letter-spacing: -3px;
    color: var(--cream);
  }
  .tagline {
    position: absolute; left: 54px; top: 138px;
    font-family: "Questrial", sans-serif; font-size: 16.5px; letter-spacing: 0.1px;
  }
  .icon-slot {
    position: absolute; left: 34px; top: 194px; width: 66px; height: 94px;
    background: var(--ink); border-radius: 30px 10px 30px 10px;
  }
  .claim-box {
    position: absolute; left: 111px; top: 196px; width: 234px; height: 90px;
    border: 2px solid var(--ink); border-radius: 14px 22px 22px 0;
    padding: 10px 0 0 15px;
    font-family: "Questrial", sans-serif; font-size: 21px; line-height: 23.5px;
    text-transform: uppercase;
  }
  .benefit {
    position: absolute; left: 40px; top: 316px; width: 300px;
    font-family: "Overlock", sans-serif; font-weight: 700;
    font-size: 20.5px; line-height: 23px; color: var(--cream);
  }
  .count {
    position: absolute; left: 104px; top: 418px;
    font-family: "Fredoka", sans-serif; font-weight: 600;
    font-size: 70px; line-height: 1; letter-spacing: -2px; color: var(--ink);
  }
  .format {
    position: absolute; left: 196px; top: 440px; width: 95px;
    border-top: 2px solid var(--ink); border-bottom: 2px solid var(--ink);
    padding: 6px 0 6px 6px;
    font-family: "Questrial", sans-serif; font-size: 15px; letter-spacing: 1px;
  }
  .net-weight {
    position: absolute; left: 104px; top: 490px;
    font-family: "Questrial", sans-serif; font-size: 15px; letter-spacing: 4px;
  }

  .swatches {
    position: absolute; top: 1063px; left: 0; width: 1200px;
    display: flex; justify-content: center; gap: 20px;
  }
  .swatch { width: 45px; height: 45px; border-radius: 50%; }
  .swatch--teal { background: linear-gradient(90deg, var(--teal) 0%, #2f5b6a 100%); }
  .swatch--slate { background: linear-gradient(90deg, var(--slate) 0%, var(--slate-dark) 100%); }
  .swatch--ink { background: var(--ink); }
  .swatch--cream { background: var(--cream); }
</style>
</head>
<body>
<main class="canvas">
  <section class="label label--slate">
    <h1 class="wordmark">velnora</h1>
    <p class="tagline">HIGH-QUALITY DAILY SUPPLEMENT</p>
    <div class="icon-slot" role="img" aria-label="Gut health icon"></div>
    <p class="claim-box">Men’s wellness<br>focused on gut<br>health.</p>
    <p class="benefit">Designed to support digestion, regularity, and internal cleanliness.</p>
    <p class="count">60</p>
    <p class="format">SOFTGELS</p>
    <p class="net-weight">NET WEIGHT: 246G</p>
  </section>

  <section class="label label--teal">
    <h1 class="wordmark">velnora</h1>
    <p class="tagline">HIGH-QUALITY DAILY SUPPLEMENT</p>
    <div class="icon-slot" role="img" aria-label="Gut health icon"></div>
    <p class="claim-box">Men’s wellness<br>focused on gut<br>health.</p>
    <p class="benefit">Designed to support digestion, regularity, and internal cleanliness.</p>
    <p class="count">60</p>
    <p class="format">SOFTGELS</p>
    <p class="net-weight">NET WEIGHT: 246G</p>
  </section>

  <div class="swatches" aria-label="Colour palette">
    <span class="swatch swatch--teal"></span>
    <span class="swatch swatch--slate"></span>
    <span class="swatch swatch--ink"></span>
    <span class="swatch swatch--cream"></span>
  </div>
</main>
</body>
</html>
```